Email Signature

We are looking for creative email signature for our company. Please find attached the logo of our company for your reference. now we understand there isn't much can be done with email signature but we are looking for out of the box designs. Nothing specific in mind

Please insert fake numbers, website and/or address, etc just to showcase the designs. once the design is chosen we will provide the actual details.
Updates

Dear All,

We wouldlike to extend our apology for not being able to provide feedbacks to everysingle design. We were extremely busy and we have multiple contests opensimultaneously which makes the process harder. However, thank you all for theefforts you have put into this contest. We have received anoverwhelming quality responses & it has been a very difficult task tochoose just one, we easily Loved at least several designs...

Thanksagain for participating, we wish you all success in your design ventures.

Kindregards,

HLW Team

Industry/Entity Type

It Company

```html
<!DOCTYPE html>
<html lang="en">
<head>
<meta charset="utf-8">
<title>Email Signature – Harbor Lantern Works</title>
<link href="https://fonts.googleapis.com/css2?family=Arimo:ital,wght@0,400;0,700;1,400&display=swap" rel="stylesheet">
<style>
  :root {
    --tag-blue: #1784de;
    --tag-blue-deep: #0f74cc;
    --tag-blue-light: #3a9cea;
    --ink-white: #ffffff;
    --brand-blue: #1a86de;
    --page: #ffffff;
  }
  * { margin: 0; padding: 0; box-sizing: border-box; }
  html, body {
    width: 1064px;
    height: 1200px;
    overflow: hidden;
    background: var(--page);
    font-family: "Arimo", Arial, sans-serif;
  }
  .signature {
    position: relative;
    width: 1064px;
    height: 1200px;
  }
  .tag {
    position: absolute;
    left: 294px;
    top: 116px;
    width: 456px;
    height: 200px;
  }
  .tag-shape { position: absolute; inset: 0; }
  .tag-text {
    position: absolute;
    right: 31px;
    top: 12px;
    text-align: right;
    color: var(--ink-white);
  }
  .person-name {
    font-size: 45px;
    font-weight: 700;
    line-height: 48px;
    letter-spacing: 0.3px;
  }
  .person-role {
    font-size: 15px;
    line-height: 16px;
    margin-bottom: 6px;
  }
  .contact-line {
    font-size: 17px;
    line-height: 21px;
    font-weight: 700;
  }
  .contact-label {
    font-weight: 400;
    font-style: italic;
    margin-right: 3px;
  }
  .contact-address {
    font-size: 16px;
    font-weight: 700;
    margin-top: 11px;
  }
  .brand-name {
    position: absolute;
    left: 0;
    width: 1064px;
    top: 372px;
    text-align: center;
    font-size: 42px;
    font-weight: 700;
    color: var(--brand-blue);
    line-height: 50px;
  }
</style>
</head>
<body>
  <main class="signature">
    <div class="tag">
      <svg class="tag-shape" viewBox="0 0 456 200" width="456" height="200" aria-hidden="true">
        <defs>
          <linearGradient id="tagFill" x1="0" y1="0" x2="0" y2="1">
            <stop offset="0" stop-color="var(--tag-blue-light)"/>
            <stop offset="0.5" stop-color="var(--tag-blue)"/>
            <stop offset="1" stop-color="var(--tag-blue-deep)"/>
          </linearGradient>
          <clipPath id="tagClip">
            <path d="M61 2 L411 2 Q454 2 454 44 L454 156 Q454 197 411 197 L61 197 Q46 197 36 184 L6 114 Q0 101 6 88 L36 16 Q46 2 61 2 Z"/>
          </clipPath>
        </defs>
        <path d="M61 2 L411 2 Q454 2 454 44 L454 156 Q454 197 411 197 L61 197 Q46 197 36 184 L6 114 Q0 101 6 88 L36 16 Q46 2 61 2 Z"
              fill="url(#tagFill)" stroke="var(--tag-blue-deep)" stroke-width="1.5"/>
        <g clip-path="url(#tagClip)">
          <ellipse cx="150" cy="-10" rx="230" ry="55" fill="#ffffff" opacity="0.22"/>
        </g>
        <circle cx="28" cy="101" r="16" fill="var(--page)"/>
      </svg>
      <div class="tag-text">
        <p class="person-name">Marcus Hale</p>
        <p class="person-role">CEO</p>
        <p class="contact-line"><span class="contact-label">phone.</span> +1 555-014-2290</p>
        <p class="contact-line"><span class="contact-label">mobile.</span> +1 555-014-2290</p>
        <p class="contact-line"><span class="contact-label">web.</span> www.harborlantern.com</p>
        <p class="contact-address">88 Pier Road #2, Portland, 04101, USA</p>
      </div>
    </div>
    <p class="brand-name">Harbor Lantern Works</p>
  </main>
</body>
</html>
```